Stylish Business Card for Modern hair salon

I need a simple business card design using our salon logo and colours that are in the logo. We service clients of all ages but predominantly those in the 18 to 55 age range. We have a young staff and are looking to have a card that will present a modern and clean image that represents who we are. The card should be in black and white same as our logo. Minimal use of other colours is allowed.

Industry/Entity Type

Hair And Beauty

Contact Information for Business Card

The design should have the following information
salon name - TR Hair Studio
address - 2751 Birchfield Rd.E. Mississauga, ON L7P3K2
phone - 905 614-2870
website - trhairexample.ca
instagram - tr.hairstudio
twitter - @TR_HairStudio

Colors
000000
ffffff
474747

Requirements
Must have
• simple design, salon name, address, phone, website, instagram, twitter info
• Back of card should have the following:
• YOUR NEXT APPOINTMENT
• DATE
• TIME
Nice to have
• simple design, clear to see and read,
• predominantly black and white colour, minimal use of other colours is ok
Should not have
• many colours, various fonts

```html
<!DOCTYPE html>
<html lang="en">
<head>
<meta charset="utf-8">
<title>TR Hair Studio – Business Card</title>
<link href="https://fonts.googleapis.com/css2?family=Lato:wght@400;700&family=Roboto+Condensed:wght@400;700&display=swap" rel="stylesheet">
<style>
  :root {
    --page: #ffffff;
    --card: #0b0b0b;
    --card-edge: #151515;
    --band: #4a4a4a;
    --white: #ffffff;
    --muted: #454545;
    --rule: #9a9a9a;
  }
  * { margin: 0; padding: 0; box-sizing: border-box; }
  html, body { width: 1200px; height: 1200px; overflow: hidden; background: var(--page); }
  body { position: relative; font-family: "Lato", sans-serif; color: var(--white); }

  .card {
    position: absolute; left: 200px; width: 800px; height: 532px;
    background: radial-gradient(ellipse at 40% 45%, var(--card-edge) 0%, var(--card) 75%);
    overflow: hidden;
  }
  .card--front { top: 46px; }
  .card--back { top: 618px; }

  .brand { position: absolute; text-align: center; }
  .brand__name {
    font-family: "Lato", sans-serif; font-weight: 700; font-size: 64px;
    line-height: 1; color: var(--white); letter-spacing: 1px; white-space: nowrap;
  }
  .card--front .brand { left: 40px; top: 100px; width: 210px; }
  .card--back .brand { left: 280px; top: 62px; width: 240px; }

  .portrait {
    position: absolute; left: 500px; top: 0; width: 300px; height: 532px;
    background: radial-gradient(ellipse at 55% 55%, #8a8a8a 0%, #3a3a3a 40%, #111 75%);
  }

  .studio-name {
    position: absolute; left: 38px; top: 240px;
    font-family: "Roboto Condensed", sans-serif; font-weight: 400;
    font-size: 58px; line-height: 1; white-space: nowrap;
  }
  .address {
    position: absolute; font-size: 17.5px; line-height: 22px; color: var(--white);
    padding-left: 16px;
  }
  .address svg { position: absolute; left: 0; top: 4px; }
  .card--front .address { left: 38px; top: 316px; }

  .band { position: absolute; background: var(--band); }
  .card--front .band { left: 0; top: 410px; width: 552px; height: 77px; }
  .card--back .band { left: 0; top: 436px; width: 800px; height: 76px; }

  .contact {
    position: absolute; display: flex; align-items: center; gap: 6px;
    font-size: 17.5px; white-space: nowrap;
  }
  .contact svg { flex: none; }
  .dot { width: 13px; height: 13px; border-radius: 50%; background: var(--white); flex: none; }

  .appointment-title {
    position: absolute; left: 0; top: 244px; width: 800px; text-align: center;
    font-family: "Roboto Condensed", sans-serif; font-weight: 700;
    font-size: 46px; line-height: 1; letter-spacing: 0.5px;
  }
  .appointment-field {
    position: absolute; top: 322px; font-size: 25px; color: var(--muted); white-space: nowrap;
  }
</style>
</head>
<body>

<section class="card card--front">
  <div class="brand"><div class="brand__name">TR Hair</div></div>
  <div class="portrait" role="img" aria-label="Black and white photo of a woman with a sleek bob haircut, seen from behind"></div>

  <h1 class="studio-name">TR Hair Studio</h1>
  <p class="address">
    <svg width="11" height="15" viewBox="0 0 11 15"><path d="M5.5 0A5.5 5.5 0 0 0 0 5.5C0 9.5 5.5 15 5.5 15S11 9.5 11 5.5A5.5 5.5 0 0 0 5.5 0Zm0 7.5a2 2 0 1 1 0-4 2 2 0 0 1 0 4Z" fill="#9a9a9a"/></svg>
    2751 Birchfield Rd.E. Mississauga,<br>ON L7P3K2
  </p>

  <div class="band"></div>
  <div class="contact" style="left:40px; top:421px;">
    <svg width="15" height="15" viewBox="0 0 24 24"><path d="M6.6 10.8a15 15 0 0 0 6.6 6.6l2.2-2.2a1 1 0 0 1 1-.25 11.4 11.4 0 0 0 3.6.57 1 1 0 0 1 1 1V20a1 1 0 0 1-1 1A17 17 0 0 1 3 4a1 1 0 0 1 1-1h3.5a1 1 0 0 1 1 1c0 1.25.2 2.45.57 3.57a1 1 0 0 1-.25 1Z" fill="#fff"/></svg>
    905 614-2870
  </div>
  <div class="contact" style="left:40px; top:456px;">
    <svg width="15" height="15" viewBox="0 0 24 24" fill="none" stroke="#fff" stroke-width="2"><circle cx="12" cy="12" r="10"/><path d="M2 12h20M12 2c3 3 3 17 0 20M12 2c-3 3-3 17 0 20"/></svg>
    trhairexample.ca
  </div>
  <div class="contact" style="left:268px; top:420px;"><span class="dot"></span>tr.hairstudio</div>
  <div class="contact" style="left:268px; top:455px;"><span class="dot"></span>@TR_HairStudio</div>
</section>

<section class="card card--back">
  <div class="brand"><div class="brand__name">TR Hair</div></div>

  <h2 class="appointment-title">YOUR NEXT APPOINTMENT</h2>
  <p class="appointment-field" style="left:126px;">DATE:&nbsp; xx-xx-xxxx</p>
  <p class="appointment-field" style="left:502px;">TIME:&nbsp; 00:00</p>

  <div class="band"></div>
  <p class="address" style="left:30px; top:450px;">
    <svg width="11" height="15" viewBox="0 0 11 15"><path d="M5.5 0A5.5 5.5 0 0 0 0 5.5C0 9.5 5.5 15 5.5 15S11 9.5 11 5.5A5.5 5.5 0 0 0 5.5 0Zm0 7.5a2 2 0 1 1 0-4 2 2 0 0 1 0 4Z" fill="#fff"/></svg>
    2751 Birchfield Rd.E. Mississauga,<br>ON L7P3K2
  </p>
  <div class="contact" style="left:371px; top:453px;">
    <svg width="15" height="15" viewBox="0 0 24 24"><path d="M6.6 10.8a15 15 0 0 0 6.6 6.6l2.2-2.2a1 1 0 0 1 1-.25 11.4 11.4 0 0 0 3.6.57 1 1 0 0 1 1 1V20a1 1 0 0 1-1 1A17 17 0 0 1 3 4a1 1 0 0 1 1-1h3.5a1 1 0 0 1 1 1c0 1.25.2 2.45.57 3.57a1 1 0 0 1-.25 1Z" fill="#fff"/></svg>
    905 614-2870
  </div>
  <div class="contact" style="left:371px; top:488px;">
    <svg width="15" height="15" viewBox="0 0 24 24" fill="none" stroke="#fff" stroke-width="2"><circle cx="12" cy="12" r="10"/><path d="M2 12h20M12 2c3 3 3 17 0 20M12 2c-3 3-3 17 0 20"/></svg>
    trhairexample.ca
  </div>
  <div class="contact" style="left:598px; top:452px;"><span class="dot"></span>tr.hairstudio</div>
  <div class="contact" style="left:598px; top:487px;"><span class="dot"></span>@TR_HairStudio</div>
</section>

</body>
</html>
```